Seafood Retailer requires varies packaging labels

We are an established business (Restaurant, Seafood Retailer and Crayfish Wholesaler). We have just got a new logo which covers all three aspects of our business (via Artbazaar!). We have always sold cellar door but have been asked by several food outlets to stock our product but as you will see from our pictures - it needs some serious work to take us to the next level. We have a well known finer dining restaurant which we use all these products in and is how several products came about on our Seafood shop shelves. The products are of high quality (just not the labelling). We now want to package our Seafood Retail Shop with professional packaging and labelling and reflect the "quality and freshness" of our products. We have several items we want to label as per below.

If we were to use a slogan it would be "Its about the Freshness and Quality" but not necessary.

We are after a label for our Pickled Seafood 350g tub (Various) - conical container 9cm high x 9cm (top), 7cm (bottom) ONLY but will also try and utilise it to be consistent with the other products following.

Salt and Pepper MIx 250g - conical container (as above)
Smoked Fish (Various weight & fish) - 21cm x 25cm vacuum sealed bags.
Kilpatrick Sauce 250ml - square bottle 22cm high x 4.5cm wide
Minty Lime Vinaigrette 250ml - 23cm round bottle - 4.7cm dia.
Smoked Spicy Salt 75g- 13cm wide x 16cm high vacuum bag
Dukkah 75g - 13cm wide x 16cm high vacuum bag
Lobster Oil 150ml - 18cm x 4.5cm dia round bottle

We will need a working file so we can change the names for the pickled seafood as needed.

I have attached photos of our current products for true understanding of what we currently have had to get by and where we wish to go.

We have a label printer that can print black type overs eg the name of each product so we can have generic coloured labels which we can print over with the change of each product.

We want something that will become a recognisable label.
Updates

Attn Designers.
We are only after one design but which we will use as a guide for all the options supplied as a starting point. The Pickled containers will probably be where we start but happy with any submissions. I probably wasnt very clear but wanted to show all the things we will be using the labelling for so that we can get some continuity We are just after some direction on a good look.  Thanks Marlo

Reason: Had some technical problems and wish to extend the time to allow more time conversing with designers.

Target Market(s)

Our target market varies but generally 30 - 65 years in the more affluent background. We are located "literally in the middle of a paddock in the middle of nowhere" (near several holiday villages) and it is the reputation of our premium, fresh products that have people returning and amazed on their first experience.

Industry/Entity Type

Restaurant

Requirements
Must have
• All:

Our logo and the colours are:
Orange
C 13%
M 79%
Y 100%
K 3%

Blue
C 100%
M 96%
Y 14%
K 3%

weight

nutrition panel, barcode (but we can also do that as a separate label on the back ourselves if needed)

"Produced & packaged by:
Harbourline Catch Pty Ltd, 40731 Pellam Highway, Tondarra SA 5592
Ph: 08 86120394"

Made in Australia from local and imported ingredients. Keep refrigerated. Store at 1oC - 4oC. Use in 7 days after opening.

Nice to have
• Pickled seafood - "Gourmet Pickled" and "Ready to Eat"
Should not have
• Use only the "Harbourline Catch" logo (not the "harbourline Restaurant & Seafood Sales or Restaurant Only logos)

```html
<!DOCTYPE html>
<html lang="en">
<head>
<meta charset="utf-8">
<title>Harbourline Catch – Salt &amp; Pepper Mix Label</title>
<link rel="stylesheet" href="https://fonts.googleapis.com/css2?family=Crimson+Text:ital,wght@0,400;0,600;1,400&family=Allura&display=swap">
<style>
  :root {
    --brand-blue: #2a2f86;
    --brand-orange: #d4561c;
    --deep-blue: #23308a;
    --mid-blue: #1f7fd0;
    --sky-blue: #2fb3ea;
    --pale-blue: #bfe8f8;
    --ribbon-light: #e6f1f7;
    --ribbon-mid: #c9dde9;
    --canvas: #ffffff;
  }
  * { margin: 0; padding: 0; box-sizing: border-box; }
  html, body {
    width: 1200px;
    height: 900px;
    overflow: hidden;
    background: var(--canvas);
  }
  .canvas {
    position: relative;
    width: 1200px;
    height: 900px;
  }
  .label {
    position: absolute;
    left: 300px;
    top: 190px;
    width: 600px;
    height: 520px;
  }
  .label-art {
    position: absolute;
    inset: 0;
    width: 600px;
    height: 520px;
  }
  .label-text {
    position: absolute;
    left: 0;
    width: 600px;
    text-align: center;
  }
  .brand-name {
    top: 150px;
    font-family: "Crimson Text", serif;
    font-weight: 600;
    font-size: 54px;
    letter-spacing: 1px;
    color: var(--brand-blue);
    display: flex;
    justify-content: center;
    align-items: center;
    gap: 14px;
  }
  .brand-dot {
    width: 18px;
    height: 18px;
    border-radius: 50%;
    background: var(--brand-orange);
  }
  .range-title {
    top: 305px;
    font-family: "Allura", cursive;
    font-size: 38px;
    color: var(--brand-blue);
    transform: rotate(-3deg);
  }
  .product-name {
    top: 398px;
    font-family: "Crimson Text", serif;
    font-size: 30px;
    color: var(--brand-blue);
  }
  .product-note {
    top: 434px;
    font-family: "Crimson Text", serif;
    font-style: italic;
    font-size: 20px;
    color: var(--brand-blue);
  }
  .net-weight {
    top: 493px;
    font-family: "Crimson Text", serif;
    font-size: 11px;
    color: var(--pale-blue);
  }
</style>
</head>
<body>
<main class="canvas">
  <section class="label">
    <svg class="label-art" viewBox="0 0 600 520" aria-hidden="true">
      <defs>
        <radialGradient id="labelGlow" cx="300" cy="190" r="340" gradientUnits="userSpaceOnUse">
          <stop offset="0" stop-color="#d8f1fb"/>
          <stop offset="0.35" stop-color="#2fb3ea"/>
          <stop offset="0.75" stop-color="#1f6fc6"/>
          <stop offset="1" stop-color="#23308a"/>
        </radialGradient>
        <linearGradient id="ribbonFade" x1="0" x2="1" y1="0" y2="0">
          <stop offset="0" stop-color="#c9dde9"/>
          <stop offset="0.5" stop-color="#f4f9fc"/>
          <stop offset="1" stop-color="#c9dde9"/>
        </linearGradient>
      </defs>
      <rect class="label-ground" x="0" y="0" width="600" height="520" fill="url(#labelGlow)"/>
      <path class="ribbon ribbon-back" d="M0 350 C150 390 250 420 300 420 C350 420 450 390 600 340 L600 420 C450 440 350 470 300 470 C250 470 150 440 0 410 Z" fill="#c9dde9" opacity="0.85"/>
      <path class="ribbon ribbon-front" d="M0 360 C150 320 240 330 300 345 C360 330 450 315 600 320 L600 390 C450 380 360 400 300 410 C240 400 150 400 0 420 Z" fill="url(#ribbonFade)" opacity="0.9"/>
      <path class="ribbon-center" d="M40 390 C160 360 230 370 300 375 C370 370 440 360 560 380 C440 450 370 470 300 472 C230 470 160 450 40 390 Z" fill="#eef6fa"/>
    </svg>

    <div class="label-text brand-name"><span>Harbourline Catch</span><span class="brand-dot"></span></div>
    <div class="label-text range-title">Gourmet Pickled Seafood</div>
    <div class="label-text product-name">Salt &amp; Pepper Mix</div>
    <div class="label-text product-note">Ready to eat</div>
    <div class="label-text net-weight">350g/12.34oz</div>
  </section>
</main>
</body>
</html>
```